Mirela Hastow ADHD coach needs a flyer

I need a flyer to be sent by email. the copy is attached. It can be changed/reduced to fit the flyer. I would like to keep my website colors. My website is www.mirelahastow.example - Thank you!

```html
<!DOCTYPE html>
<html lang="en">
<head>
<meta charset="utf-8">
<title>Mirela Hastow – ADHD and Academic Coach Flyer</title>
<link rel="stylesheet" href="https://fonts.googleapis.com/css2?family=Jost:ital,wght@0,300;0,400;0,500;0,700;1,300;1,400;1,700&display=swap">
<style>
:root{
  --brand:#98b4c0;
  --brand-deep:#8fafbb;
  --slate:#7d8183;
  --panel:#eff0f0;
  --ink:#1d1d1d;
  --body:#333;
  --white:#fff;
  --backdrop:#b9babd;
}
*{box-sizing:border-box;margin:0;padding:0}
html,body{width:1200px;height:2400px;overflow:hidden}
body{background:var(--backdrop);font-family:"Jost",sans-serif;color:var(--body);position:relative}
.page{position:absolute;left:191px;width:877px;height:1133px;background:var(--white);transform:scale(.9317);transform-origin:0 0;overflow:hidden}
.page--one{top:79px}
.page--two{top:1241px}
.band{position:absolute;left:0;width:100%;height:12px;background:var(--brand)}
.band--top{top:0}
.band--bottom{bottom:0}
.abs{position:absolute}
.photo{position:absolute}
.headline{left:0;top:30px;width:100%;text-align:center;color:var(--brand);font-weight:700;font-size:31px;line-height:37px;letter-spacing:1px}
.headline-rule{top:89px;height:1.5px;background:var(--brand)}
.name-band{left:22px;top:441px;width:381px;height:65px;background:var(--slate);color:var(--white);text-align:center}
.name-band__name{font-size:25px;letter-spacing:3px;font-weight:400;margin-top:8px;display:flex;align-items:center;justify-content:center;gap:12px}
.name-band__name::before,.name-band__name::after{content:"";width:28px;height:2.5px;background:var(--white)}
.name-band__title{font-size:11.5px;font-style:italic;margin-top:1px}
.focus-box{left:22px;top:506px;width:381px;height:250px;background:var(--brand-deep);color:var(--white);text-align:center;padding:26px 30px 0}
.focus-box h2{font-size:24px;letter-spacing:1.5px;font-weight:700}
.focus-box .sub{font-size:18px;font-style:italic;font-weight:300;margin-top:2px}
.focus-box .sub b{font-style:normal;font-weight:700}
.focus-box .rule{width:36px;height:3px;background:var(--white);margin:7px auto 16px}
.focus-box p{font-size:15px;line-height:21px;font-weight:300}
.intro{left:427px;top:128px;width:430px;text-align:center;font-size:17.5px;line-height:22px;color:var(--ink)}
.intro-rule{left:620px;top:229px;width:40px;height:2px;background:var(--brand)}
.copy{left:427px;top:239px;width:430px;font-size:15.3px;line-height:20.6px;text-align:justify;color:var(--ink);font-weight:400}
.copy p+p{margin-top:14px}
.positioned{left:22px;top:756px;width:835px;height:357px;background:var(--panel)}
.positioned h2{position:absolute;left:40px;top:8px;font-size:25px;line-height:31px;text-align:center;color:var(--ink);letter-spacing:1.3px;font-weight:700}
.bullets{list-style:none}
.bullets li{position:relative;padding-left:20px;color:var(--ink)}
.bullets li::before{content:"";position:absolute;left:0;top:6px;width:10px;height:10px;background:var(--brand)}
.positioned .bullets{position:absolute;left:18px;top:82px;font-size:15.5px;line-height:21px}
.positioned .bullets li{margin-bottom:8px}
.positioned .bullets li.narrow{width:425px}
.url-tab{left:280px;top:1100px;width:315px;height:21px;background:var(--brand);clip-path:polygon(18px 0,calc(100% - 18px) 0,100% 100%,0 100%)}
.url-tab--inner{left:294px;top:1100px;width:287px;height:22px;background:var(--panel);clip-path:polygon(12px 0,calc(100% - 12px) 0,100% 100%,0 100%);text-align:center;font-size:17px;letter-spacing:1.5px;color:var(--ink);line-height:22px}
.potential-box{left:22px;top:200px;width:406px;height:118px;background:var(--brand-deep);color:var(--white);text-align:center;padding-top:12px}
.potential-box h2{font-size:25px;letter-spacing:1.5px;font-weight:700}
.potential-box p{font-size:18px;line-height:24px;font-style:italic;font-weight:300;margin-top:2px}
.potential-box .rule{width:36px;height:3px;background:var(--white);margin:3px auto 0}
.list-two{left:22px;font-size:15.5px;line-height:20px}
.list-two li{margin-bottom:7.4px}
.have-box{left:23px;top:475px;width:405px;height:48px;background:var(--brand-deep);color:var(--white);font-size:25px;font-weight:700;letter-spacing:1.5px;text-align:center;line-height:48px}
.quote{top:682px;width:398px;height:283px;background:var(--panel);border-top:1.5px solid var(--brand)}
.quote--parents{left:22px}
.quote--students{left:458px}
.quote-mark{top:666px;width:38px;height:36px;background:var(--brand)}
.quote h3{text-align:center;font-size:25px;letter-spacing:1.2px;color:var(--ink);font-weight:700;margin-top:14px}
.quote .q{font-size:15.5px;line-height:20.6px;font-style:italic;font-weight:300;color:var(--ink);padding:0 18px;margin-top:14px}
.quote .q b{font-weight:700}
.quote .q+.q{margin-top:12px}
.quote--parents .q+.q{margin-top:0}
.next h2{position:absolute;left:0;top:982px;width:100%;text-align:center;font-size:26px;letter-spacing:1.5px;color:var(--ink);font-weight:700}
.next-rule{top:999px;height:1.5px;background:var(--brand)}
.next .lead{position:absolute;left:0;top:1023px;width:100%;text-align:center;font-size:18px;font-style:italic;font-weight:300;letter-spacing:.5px;color:var(--ink)}
.contact{top:1056px;font-size:19px;font-weight:700;letter-spacing:1.3px;color:var(--ink)}
.icon-tab{top:1096px;width:70px;height:25px;background:var(--brand);clip-path:polygon(14px 0,56px 0,100% 100%,0 100%);display:flex;align-items:center;justify-content:center;padding-top:4px}
</style>
</head>
<body>

<section class="page page--one">
  <div class="band band--top"></div>
  <h1 class="abs headline">Helping Your Child with ADHD or Other Learning<br>Challenges Thrive in College and Beyond</h1>
  <div class="abs headline-rule" style="left:0;width:100px"></div>
  <div class="abs headline-rule" style="left:777px;width:100px"></div>

  <div class="photo" role="img" aria-label="Portrait of the coach in a pale pink blazer, arms crossed, against a grey wall" style="left:22px;top:131px;width:381px;height:310px;background:linear-gradient(160deg,#a9aeb1,#8f9497 60%,#7e8386)"></div>
  <div class="abs name-band">
    <div class="name-band__name">MIRELA HASTOW</div>
    <div class="name-band__title">Ph.D. &nbsp;|&nbsp; ADHD and Academic Coach</div>
  </div>
  <div class="abs focus-box">
    <h2>Empowering Focus:</h2>
    <div class="sub">How <b>Mirela</b> Helps</div>
    <div class="rule"></div>
    <p>Mirela has taken students from failing to a 3.0 GPA, and from a C student to the Dean’s List, in just one semester. It doesn’t take years to provide lasting results; all it takes is the right guide.</p>
  </div>

  <p class="abs intro">Academic success coaching that leads to lifelong transformation for students with ADHD and similar challenges that may have impeded their ability to thrive.</p>
  <div class="abs intro-rule"></div>
  <div class="abs copy">
    <p>Sending your child off to college can feel scary, especially if that college is hundreds of miles away. You worry about how they’ll do on their own—whether they’ll make friends, earn good grades, and be happy—especially without you there to support them daily. You know your child is bright, and you want them to have a great future, but you’re concerned they will struggle without the right support and resources.</p>
    <p>You don’t need to feel helpless as you send your child off to this next stage of their lives. Mirela is dedicated to making that transition easier for everyone. Mirela Hastow has years of experience helping students thrive despite their challenges. She sees your child’s potential and helps them see it, too. She provides a safety net as they adjust to a new environment at college. Her services are comprehensive and adaptable, based on the requirements of each individual: helping with course selection and scheduling, time management, study strategies, focus, making new friends, and adapting to change. Through it all, Mirela guides students through fundamental work on mindset to ensure that changes stick.</p>
  </div>

  <div class="abs positioned">
    <h2>Uniquely positioned to<br>help your child, Mirela:</h2>
    <ul class="bullets">
      <li class="narrow">Tailors support so that your child improves focus and maximizes their potential in college and beyond.</li>
      <li class="narrow">Understands your child’s unique needs - she sees the gifts that others often miss.</li>
      <li>Knows the academic landscape intimately, including the challenges faced by students with ADHD and other conditions.</li>
      <li>Helps with the logistics of scheduling in a way that most advisors can’t, enrolling students in the courses that best suit their learning style.</li>
      <li>Nurtures the brilliance in your bright child.</li>
      <li>Provides a balance between encouraging students and challenging them.</li>
    </ul>
  </div>
  <div class="photo" role="img" aria-label="Three students studying together at a table by a bright window" style="left:470px;top:728px;width:387px;height:184px;background:linear-gradient(120deg,#d7dde0,#9aa6ad 45%,#6f8f99 70%,#c9d2d6)"></div>

  <div class="abs url-tab"></div>
  <div class="abs url-tab--inner">www.mirelahastow.example</div>
  <div class="band band--bottom"></div>
</section>

<section class="page page--two">
  <div class="band band--top"></div>
  <div class="photo" role="img" aria-label="Group of smiling college students sitting together outdoors with tablets and laptops" style="left:0;top:12px;width:877px;height:254px;background:linear-gradient(90deg,#dfe6e3,#c8a591 30%,#d9b66a 55%,#8aa06a 80%,#4f7a46)"></div>
  <div class="abs potential-box">
    <h2>Realizing Potential:</h2>
    <p>The Transformation<br>You’ll See in Your Child</p>
    <div class="rule"></div>
  </div>

  <ul class="abs bullets list-two" style="top:331px">
    <li>A mindset of self-belief and increased confidence.</li>
    <li>Higher grades and the drive to graduate.</li>
    <li>Social integration and making friends.</li>
    <li>Happiness and fulfilment.</li>
    <li>A deep sense of personal achievement and pride.</li>
  </ul>
  <div class="abs have-box">You Will Have:</div>
  <ul class="abs bullets list-two" style="top:538px">
    <li>Less stress, knowing that your child is in good hands.</li>
    <li>Fewer sleepless nights worrying about your child.</li>
    <li>Confidence that they are receiving the right support.</li>
    <li>Joy and pride at seeing them do well.</li>
  </ul>

  <div class="photo" role="img" aria-label="Graduates tossing their caps into a bright sky" style="left:471px;top:286px;width:372px;height:360px;background:linear-gradient(180deg,#eef2f7,#bfcde0 55%,#3c4a6a)"></div>

  <div class="abs quote quote--parents">
    <h3>What Parents Say</h3>
    <p class="q">“Mirela was the glue that kept our daughter in college… as our daughter’s Academic Coach, [she] gave our daughter the ability to finish strong by empowering her with the skills needed to be successful.”—<b>Renata</b></p>
    <p class="q">“Mirela has always told my daughter not that she can succeed, but that she will succeed.”—<b>Lucille</b></p>
  </div>
  <div class="abs quote quote--students">
    <h3>What Students Say</h3>
    <p class="q">"Last semester I completed all 16 hours and I had the highest GPA I’ve ever had!”<br>—<b>Former student</b></p>
    <p class="q">“Under her instruction, my grades began to improve. I ended up making the Dean’s List during my time at Ridgefield, and I was also inducted into the Civic Honors Society. I am currently in my first year of law school at Harlow State University, a top tier school.”—<b>Former student</b></p>
  </div>
  <div class="abs quote-mark" style="left:36px"><svg width="38" height="36" viewBox="0 0 38 36"><path d="M11 12h5l-3 6h3v7h-7v-6zM21 12h5l-3 6h3v7h-7v-6z" fill="#fff"/></svg></div>
  <div class="abs quote-mark" style="left:472px"><svg width="38" height="36" viewBox="0 0 38 36"><path d="M11 12h5l-3 6h3v7h-7v-6zM21 12h5l-3 6h3v7h-7v-6z" fill="#fff"/></svg></div>

  <div class="next">
    <div class="abs next-rule" style="left:22px;width:318px"></div>
    <h2>Next Steps</h2>
    <div class="abs next-rule" style="left:543px;width:313px"></div>
    <p class="lead">To learn more and discuss your child’s individual needs, call</p>
  </div>
  <div class="abs contact" style="left:110px;top:1060px">555•010•4821</div>
  <div class="abs contact" style="left:301px">coach@mirelahastow.example</div>
  <div class="abs contact" style="left:612px">mirelahastow.example</div>

  <div class="abs icon-tab" style="left:158px"><svg width="16" height="16" viewBox="0 0 24 24"><path d="M6.6 10.8a15 15 0 0 0 6.6 6.6l2.2-2.2a1 1 0 0 1 1-.25 11.4 11.4 0 0 0 3.6.6 1 1 0 0 1 1 1V20a1 1 0 0 1-1 1A17 17 0 0 1 3 4a1 1 0 0 1 1-1h3.5a1 1 0 0 1 1 1c0 1.25.2 2.45.6 3.6a1 1 0 0 1-.25 1z" fill="#fff"/></svg></div>
  <div class="abs icon-tab" style="left:403px"><svg width="18" height="14" viewBox="0 0 18 14"><rect x="1" y="1" width="16" height="12" fill="#fff"/><path d="M1 1l8 6 8-6" fill="none" stroke="#98b4c0" stroke-width="1.4"/></svg></div>
  <div class="abs icon-tab" style="left:640px"><svg width="17" height="17" viewBox="0 0 24 24" fill="none" stroke="#fff" stroke-width="2"><circle cx="12" cy="12" r="9"/><path d="M3 12h18M12 3c3 3 3 15 0 18M12 3c-3 3-3 15 0 18"/></svg></div>
  <div class="band band--bottom"></div>
</section>

</body>
</html>
```